Professional Photography Business cards

I need business cards that include my logo which I have uploaded. I run a photography business. I am open to ideas but I would like one side to have my logo and the other side to have my contact info. I don't have a website made but I do own a website domain. I have uploaded 2 different logo color schemes. My business colors are Blue, black , and white.

Business Name
Business Phone Number
Business Email
Business Website address
Instagram

Industry/Entity Type

Professional Photography

Contact Information for Business Card

Phone Number: 555-314-8027 email: info@tkellan-studios.example Instagram: @t.kellanstudios website doman- www.tkellan-studios.example

Requirements
Must have
• I like the idea of a business card with a full black background front and back of card. My colors must include royal blue, black, and white

```html
<!DOCTYPE html>
<html lang="en">
<head>
<meta charset="UTF-8">
<title>T. Kellan Studios – Business Card</title>
<link href="https://fonts.googleapis.com/css2?family=Open+Sans:wght@400&display=swap" rel="stylesheet">
<style>
  :root {
    --page-bg: #2a2a2c;
    --card-black: #141415;
    --royal-blue: #2f3ad1;
    --ink-white: #ffffff;
    --foil-grey: #8d8d92;
  }
  * { margin: 0; padding: 0; box-sizing: border-box; }
  html, body {
    width: 1200px; height: 900px; overflow: hidden;
    background: var(--page-bg);
    font-family: "Open Sans", sans-serif;
  }
  .sheet {
    width: 1200px; height: 900px;
    display: flex; flex-direction: column;
    align-items: center; justify-content: center; gap: 60px;
  }
  .card {
    position: relative;
    width: 630px; height: 360px;
    background: var(--card-black);
    border-radius: 22px;
    box-shadow: 0 18px 40px rgba(0,0,0,0.55);
  }
  .brand {
    position: absolute;
    display: flex; align-items: center; gap: 16px;
    font-size: 34px; letter-spacing: 0.04em;
    white-space: nowrap;
  }
  .brand-dot {
    width: 46px; height: 46px; border-radius: 50%;
    border: 3px solid currentColor;
  }
  .card-front .brand {
    color: var(--foil-grey);
    left: 50%; top: 50%; transform: translate(-50%, -50%);
  }
  .card-back .brand {
    color: var(--ink-white);
    left: 150px; top: 60px;
  }
  .contact-list {
    position: absolute; left: 290px; top: 190px;
    list-style: none;
    color: var(--ink-white);
    font-size: 19px; line-height: 32px;
  }
  .contact-item { display: flex; align-items: center; gap: 12px; }
  .contact-icon { width: 18px; height: 18px; flex: none; }
</style>
</head>
<body>
<main class="sheet">
  <section class="card card-front" aria-label="Card front">
    <div class="brand"><span class="brand-dot"></span><span class="brand-name">T. Kellan Studios</span></div>
  </section>

  <section class="card card-back" aria-label="Card back">
    <div class="brand"><span class="brand-dot"></span><span class="brand-name">T. Kellan Studios</span></div>
    <ul class="contact-list">
      <li class="contact-item">
        <svg class="contact-icon" viewBox="0 0 24 24"><path fill="var(--royal-blue)" d="M6.6 10.8a15 15 0 0 0 6.6 6.6l2.2-2.2a1 1 0 0 1 1-.25 11.4 11.4 0 0 0 3.6.57 1 1 0 0 1 1 1V20a1 1 0 0 1-1 1A17 17 0 0 1 3 4a1 1 0 0 1 1-1h3.5a1 1 0 0 1 1 1c0 1.25.2 2.45.57 3.57a1 1 0 0 1-.25 1z"/></svg>
        <span>555-314-8027</span>
      </li>
      <li class="contact-item">
        <svg class="contact-icon" viewBox="0 0 24 24"><rect x="2" y="5" width="20" height="14" rx="1" fill="var(--royal-blue)"/><path d="M2 6l10 7 10-7" fill="none" stroke="var(--card-black)" stroke-width="1.6"/></svg>
        <span>info@tkellan-studios.example</span>
      </li>
      <li class="contact-item">
        <svg class="contact-icon" viewBox="0 0 24 24"><g fill="none" stroke="var(--royal-blue)" stroke-width="2"><circle cx="12" cy="12" r="9"/><ellipse cx="12" cy="12" rx="4" ry="9"/><path d="M3 12h18"/></g></svg>
        <span>www.tkellan-studios.example</span>
      </li>
      <li class="contact-item">
        <svg class="contact-icon" viewBox="0 0 24 24"><circle cx="12" cy="12" r="8" fill="none" stroke="var(--royal-blue)" stroke-width="2.4"/></svg>
        <span>@t.kellanstudios</span>
      </li>
    </ul>
  </section>
</main>
</body>
</html>
```